Firm Stationery Design

I need a design for stationery, including: Stationery First Page, Stationery Second Sheet, Envelope, Mailing Label for Flat Envelopes, and Business Cards

```html
<!DOCTYPE html>
<html lang="en">
<head>
<meta charset="utf-8">
<title>Harlow Legal – Stationery</title>
<link rel="stylesheet" href="https://fonts.googleapis.com/css2?family=Poppins:wght@400;500;600;700&display=swap">
<style>
  :root{
    --orange:#f59a0a;
    --ink:#1c1c1c;
    --card:#202020;
    --paper:#ffffff;
    --stage:#aaaaaa;
    --muted:#555555;
    --faint:#eeeeee;
  }
  *{box-sizing:border-box;margin:0;padding:0}
  html,body{width:1200px;height:2274px;overflow:hidden}
  body{background:var(--stage);font-family:"Poppins",sans-serif;color:var(--ink);position:relative}
  .sheet-set{position:absolute;left:40px;top:430px;width:974px;height:1229px;transform:scale(1.15);transform-origin:0 0}
  .piece{position:absolute;background:var(--paper);box-shadow:4px 6px 10px rgba(0,0,0,.25);overflow:hidden}

  .letter{width:464px;height:602px;left:0}
  .letter--first{top:0}
  .letter--second{top:627px}
  .band-top{position:absolute;left:0;top:0;width:100%;height:55px;
    background:linear-gradient(90deg,var(--ink) 0 8%,var(--orange) 8% 16%,var(--ink) 16% 24%,var(--orange) 24% 32%,var(--ink) 32% 40%,var(--orange) 40% 48%,var(--ink) 48% 56%,var(--orange) 56% 64%,var(--ink) 64% 72%,var(--orange) 72% 80%,var(--ink) 80% 88%,var(--orange) 88% 100%)}
  .band-bottom{position:absolute;left:64px;bottom:0;width:336px;height:13px;
    background:repeating-linear-gradient(90deg,var(--orange) 0 9px,var(--ink) 9px 18px)}

  .brand{position:absolute;display:flex;align-items:center;gap:6px;font-weight:700;color:var(--ink);white-space:nowrap}
  .brand::before{content:"";width:10px;height:10px;background:var(--orange)}
  .letter .brand{left:48px;font-size:19px}
  .letter--first .brand{top:145px}
  .letter--second .brand{top:48px}

  .recipient{position:absolute;left:48px;top:205px;font-size:9px;line-height:1.35}
  .recipient strong{display:block;font-weight:600;font-size:9.5px;margin-bottom:10px}
  .body-copy{position:absolute;left:48px;top:283px;width:368px;font-size:6.2px;line-height:1.28;color:#333}
  .body-copy p{margin-bottom:14px}
  .closing{position:absolute;left:48px;top:455px;font-size:7px}
  .signature{display:block;width:90px;height:18px;margin:10px 0 6px;background:linear-gradient(90deg,#3a3a3a22,#3a3a3a55,#3a3a3a22);border-radius:9px}
  .closing strong{display:block;font-weight:600;font-size:7.5px}
  .closing span{font-size:6.5px}

  .contact-rule{position:absolute;left:48px;width:368px;height:1px;background:var(--orange)}
  .letter--first .contact-rule{top:537px}
  .letter--second .contact-rule{top:554px}
  .contact-row{position:absolute;left:48px;width:368px;display:flex;justify-content:space-between;font-size:6px;color:#333}
  .letter--first .contact-row{top:552px}
  .letter--second .contact-row{top:569px}
  .contact-row span{display:flex;align-items:center;gap:3px}
  .icon{width:7px;height:7px;fill:var(--orange);flex:none}

  .watermark{position:absolute;left:96px;top:197px;width:272px;height:260px;background:linear-gradient(135deg,#ececec,#f7f7f7)}

  .biz-card{width:334px;height:190px;left:511px;background:radial-gradient(circle at 40% 50%,#2a2a2a,var(--card));color:#fff}
  .biz-card--front{top:221px}
  .biz-card--back{top:452px}
  .biz-card .brand{color:#fff}
  .biz-card--front .brand{left:16px;top:60px;font-size:15px}
  .biz-card--back .brand{left:20px;top:80px;font-size:21px}
  .card-edge{position:absolute;right:22px;top:0;width:1px;height:160px;background:var(--orange);opacity:.6}
  .card-person{position:absolute;right:32px;top:16px;font-size:12.5px;line-height:1.15}
  .card-person strong{font-weight:700;display:block}
  .card-person .surname{color:var(--orange);font-weight:400}
  .card-person em{font-style:normal;font-size:9.5px;display:block;margin-top:2px}
  .card-contacts{position:absolute;left:16px;top:110px;font-size:8px;line-height:2}
  .card-contacts span{display:flex;align-items:center;gap:6px}
  .card-contacts .icon{width:9px;height:9px}
  .card-web{position:absolute;left:16px;bottom:14px;font-size:8.5px;letter-spacing:1.3px;display:flex;align-items:center;gap:6px;width:226px}
  .card-web b{color:var(--orange);font-weight:600}
  .card-web::after{content:"";flex:1;height:1px;background:var(--orange)}
  .card-mark{position:absolute;right:0;bottom:0;width:88px;height:84px;background:linear-gradient(90deg,#ffffff 0 50%,#3a3a3a 50% 100%)}

  .envelope{width:463px;height:325px;left:511px;top:683px}
  .envelope-band{position:absolute;left:37px;top:0;width:37px;height:100%;
    background:repeating-linear-gradient(180deg,var(--orange) 0 14px,var(--ink) 14px 28px)}
  .envelope .brand{right:36px;top:70px;font-size:23px}
  .envelope-contacts{position:absolute;right:36px;top:270px;display:flex;gap:14px;font-size:9px;color:#333}
  .envelope-contacts span{display:flex;align-items:center;gap:4px}
  .envelope-contacts .icon{width:9px;height:9px}
</style>
</head>
<body>
<svg width="0" height="0" style="position:absolute">
  <symbol id="i-phone" viewBox="0 0 10 10"><path d="M2 0.5l2 2-1 1.2c.6 1.3 1.6 2.3 2.9 2.9L7 5.6l2 2L7.8 9.5C4 9 1 6 .5 2.2z"/></symbol>
  <symbol id="i-mail" viewBox="0 0 10 10"><path d="M0 2h10v6H0zM0.8 2.6L5 5.6l4.2-3v-.2H.8z"/></symbol>
  <symbol id="i-web" viewBox="0 0 10 10"><circle cx="5" cy="5" r="4.5"/></symbol>
  <symbol id="i-pin" viewBox="0 0 10 10"><path d="M5 0a3.5 3.5 0 0 1 3.5 3.5C8.5 6 5 10 5 10S1.5 6 1.5 3.5A3.5 3.5 0 0 1 5 0zm0 2a1.5 1.5 0 1 0 0 3 1.5 1.5 0 0 0 0-3z"/></symbol>
</svg>

<main class="sheet-set">
  <section class="piece letter letter--first">
    <div class="band-top" role="img" aria-label="Black and orange chevron header pattern"></div>
    <div class="brand">Harlow Legal</div>
    <div class="recipient">
      <strong>Renata L. Ashford</strong>
      Advocate<br>2210 Marlow Street<br>Easton, PA 18042
    </div>
    <div class="body-copy">
      <p>We write to confirm receipt of your documents and to outline the next steps in your matter. Our team has reviewed each file with care and prepared a short summary of the key points. Please read the notes below and contact our office with any questions before the scheduled meeting date next month.</p>
      <p>The filing deadline remains unchanged, and we expect the court to respond within the usual period. In the meantime we will gather the remaining records and speak with the parties named in the agreement. You will receive a full written update as soon as each stage of the review is complete and signed off.</p>
      <p>Thank you for placing your trust in our firm. We value the opportunity to represent you and will keep you informed at every stage. Should anything change on your side, simply reply to this letter or call our office directly, and a member of the team will be glad to assist you promptly.</p>
    </div>
    <div class="closing">
      Sincerely Yours,
      <span class="signature" role="img" aria-label="Handwritten signature"></span>
      <strong>Celia M. Ward</strong>
      <span>Managing director</span>
    </div>
    <div class="contact-rule"></div>
    <div class="contact-row">
      <span><svg class="icon"><use href="#i-phone"/></svg>555 01 2468</span>
      <span><svg class="icon"><use href="#i-mail"/></svg>info@harlowlegal.com</span>
      <span><svg class="icon"><use href="#i-web"/></svg>www.harlowlegal.com</span>
      <span><svg class="icon"><use href="#i-pin"/></svg>2210 Marlow Street Easton, PA 18042</span>
    </div>
    <div class="band-bottom" role="img" aria-label="Orange and black slanted stripe pattern"></div>
  </section>

  <section class="piece letter letter--second">
    <div class="brand">Harlow Legal</div>
    <div class="watermark" role="img" aria-label="Faint brand decoration"></div>
    <div class="contact-rule"></div>
    <div class="contact-row">
      <span><svg class="icon"><use href="#i-phone"/></svg>555 01 2468</span>
      <span><svg class="icon"><use href="#i-mail"/></svg>info@harlowlegal.com</span>
      <span><svg class="icon"><use href="#i-web"/></svg>www.harlowlegal.com</span>
      <span><svg class="icon"><use href="#i-pin"/></svg>2210 Marlow Street Easton, PA 18042</span>
    </div>
  </section>

  <section class="piece biz-card biz-card--front">
    <div class="brand">Harlow Legal</div>
    <div class="card-edge"></div>
    <div class="card-person">
      <strong>Renata</strong>
      <span class="surname">L. Ashford</span>
      <em>Advocate</em>
    </div>
    <div class="card-contacts">
      <span><svg class="icon"><use href="#i-phone"/></svg>555 01 2468</span>
      <span><svg class="icon"><use href="#i-mail"/></svg>info@harlowlegal.com</span>
      <span><svg class="icon"><use href="#i-pin"/></svg>2210 Marlow Street Easton, PA 18042</span>
    </div>
    <div class="card-web">www.<b>harlowlegal</b>.com</div>
    <div class="card-mark" role="img" aria-label="Brand decoration in white and grey"></div>
  </section>

  <section class="piece biz-card biz-card--back">
    <div class="brand">Harlow Legal</div>
    <div class="card-edge"></div>
    <div class="card-web">www.<b>harlowlegal</b>.com</div>
    <div class="card-mark" role="img" aria-label="Brand decoration in white and grey"></div>
  </section>

  <section class="piece envelope">
    <div class="envelope-band" role="img" aria-label="Orange and black chevron side pattern"></div>
    <div class="brand">Harlow Legal</div>
    <div class="envelope-contacts">
      <span><svg class="icon"><use href="#i-phone"/></svg>555 01 2468</span>
      <span><svg class="icon"><use href="#i-mail"/></svg>info@harlowlegal.com</span>
      <span><svg class="icon"><use href="#i-web"/></svg>www.harlowlegal.com</span>
    </div>
  </section>
</main>
</body>
</html>
```